Vexor Mind Social Media Advertisement

We need a social media advertisement made up for our Asset Insight. Our initial campaign will be on Reddit, so it needs to be compliant with reddit. Attached is a brief, we just need 1 single design initially that we can interchange the copy to see what converts better. Must be in a format that we can easily edit. Attached also are some examples of advertisements that are currently posted on Reddit for similar products. Coinsprig is the closest competitor. Please visit our website: https://www.vexormind.example to understand more about the business. You can also register as a free user to view the platform.

Target Market(s)

Self-directed Australian investors — particularly Self managed super fund trustees and property investors — who actively manage their own wealth and want AI-powered insights to make smarter financial decisions.

Industry/Entity Type

Financial technology (FinTech) / Wealth management software.

Requirements
Must have
• Dark, sophisticated colour palette (navy and teal), no emoji or decorative icons, clean and modern typography, and imagery that conveys intelligence, data, and financial confidence — not generic stock market clichés.
Nice to have
• Subtle futuristic or tech aesthetic, data visualisation elements (charts, graphs, network nodes), a sense of calm authority rather than aggressive "get rich" energy, and designs that would work across both digital ads and print formats.
Should not have
• Bright or garish colours, cartoonish illustrations, generic stock market imagery (bulls, bears, ticker tape), cluttered layouts, anything that feels salesy or hype-driven, and no cryptocurrency or "get rich quick" visual cues.

```html
<!DOCTYPE html>
<html lang="en">
<head>
<meta charset="utf-8">
<title>Vexor Mind — Asset Insight social ads</title>
<link rel="stylesheet" href="https://fonts.googleapis.com/css2?family=Inter+Tight:wght@600;700&family=Inter:wght@400;500;700&display=swap">
<style>
  :root {
    --page: #ffffff;
    --navy-deep: #0b1424;
    --navy-mid: #102646;
    --navy-glow: #173a66;
    --white: #ffffff;
    --teal: #2ad4bd;
    --violet: #6a6fc2;
    --road-dark: #1c2530;
    --road-light: #3c4654;
  }
  * { margin: 0; padding: 0; box-sizing: border-box; }
  html, body { width: 1200px; height: 831px; overflow: hidden; background: var(--page); }
  .sheet { position: relative; width: 1200px; height: 831px; }

  .ad {
    position: absolute;
    overflow: hidden;
    background:
      radial-gradient(ellipse 70% 60% at 75% 65%, var(--navy-glow) 0%, transparent 70%),
      linear-gradient(180deg, var(--navy-deep) 0%, var(--navy-mid) 100%);
    color: var(--white);
  }
  .ad--square { width: 400px; height: 400px; }
  .ad--wide { width: 764px; height: 400px; }
  .pos-tl { left: 13px; top: 11px; }
  .pos-tr { left: 423px; top: 11px; }
  .pos-bl { left: 13px; top: 420px; }
  .pos-br { left: 423px; top: 420px; }

  .scene {
    position: absolute;
    background: linear-gradient(150deg, transparent 25%, var(--road-light) 48%, var(--road-dark) 60%, transparent 80%);
    opacity: 0.55;
  }
  .ad--square .scene { left: 0; top: 180px; width: 400px; height: 220px; }
  .ad--wide .scene { left: 420px; top: 190px; width: 344px; height: 210px; }

  .headline {
    position: absolute;
    font-family: "Inter Tight", sans-serif;
    font-weight: 700;
    letter-spacing: -0.045em;
  }
  .ad--square .headline { left: 29px; top: 36px; font-size: 28px; line-height: 30.5px; }
  .ad--wide .headline { left: 47px; top: 28px; font-size: 48px; line-height: 52px; }

  .headline__contrast {
    display: block;
    background: linear-gradient(90deg, var(--teal) 0%, var(--teal) 35%, var(--violet) 100%);
    -webkit-background-clip: text;
    background-clip: text;
    color: transparent;
    width: max-content;
  }
  .ad--square .headline__contrast { margin-top: 7px; }
  .ad--wide .headline__contrast { margin-top: 7px; }

  .tagline {
    position: absolute;
    font-family: "Inter", sans-serif;
    font-weight: 500;
  }
  .ad--square .tagline { left: 29px; top: 203px; font-size: 10.5px; }
  .ad--wide .tagline { left: 50px; top: 305px; font-size: 17.5px; letter-spacing: 0.01em; }

  .support {
    position: absolute;
    left: 47px; top: 287px;
    font-family: "Inter", sans-serif;
    font-size: 18px;
    line-height: 24px;
    letter-spacing: 0.01em;
  }
  .support__lead { font-weight: 400; }
  .support__action { font-weight: 700; }

  .brand {
    position: absolute;
    font-family: "Inter Tight", sans-serif;
    font-weight: 600;
    letter-spacing: -0.03em;
    color: var(--white);
    white-space: nowrap;
  }
  .ad--square .brand { right: 28px; top: 350px; font-size: 25px; }
  .ad--wide .brand { right: 44px; top: 350px; font-size: 25px; }
</style>
</head>
<body>
<main class="sheet">

  <section class="ad ad--square pos-tl">
    <div class="scene" role="img" aria-label="Silver electric car on a dark road at a fork, a glass thumbs-up marker on the road ahead"></div>
    <h1 class="headline">Trusted investment<br>intelligence filtered for<br>your portfolio.<span class="headline__contrast">Not the crowd’s.</span></h1>
    <p class="tagline">Your portfolio. Your signals. Your edge.</p>
    <p class="brand">Vexor Mind</p>
  </section>

  <section class="ad ad--wide pos-tr">
    <div class="scene" role="img" aria-label="Silver electric car on a dark road at a fork, a glass thumbs-up marker on the road ahead"></div>
    <h2 class="headline">Trusted investment<br>intelligence filtered for<br>your portfolio.<span class="headline__contrast">Not the crowd’s.</span></h2>
    <p class="tagline">Your portfolio. Your signals. Your edge.</p>
    <p class="brand">Vexor Mind</p>
  </section>

  <section class="ad ad--square pos-bl">
    <div class="scene" role="img" aria-label="Silver electric car on a dark road at a fork, a glass thumbs-up marker on the road ahead"></div>
    <h2 class="headline">Trusted investment<br>intelligence filtered for<br>your portfolio.<span class="headline__contrast">Not the crowd’s.</span></h2>
    <p class="tagline">Your portfolio. Your signals. Your edge.</p>
    <p class="brand">Vexor Mind</p>
  </section>

  <section class="ad ad--wide pos-br">
    <div class="scene" role="img" aria-label="Silver electric car on a dark road at a fork, a glass thumbs-up marker on the road ahead"></div>
    <h2 class="headline">Trusted investment<br>intelligence filtered for<br>your portfolio.<span class="headline__contrast">Not the crowd’s.</span></h2>
    <p class="support"><span class="support__lead">Stop reading what everyone else reads.</span><br><span class="support__action">Get intelligence that’s relevant to you.</span></p>
    <p class="brand">Vexor Mind</p>
  </section>

</main>
</body>
</html>
```